Tasteful instructions for employees/guests to wash hands

Need an aesthetic visualisation of steps to wash hands.
While we would like to convey the proper steps to wash hands we also don't want to treat our staff/guests like children, rather provide a quick reminder.
Suggested sizes
16″ × 24″
11″ × 14″
A simplified version of these steps:
- Wet your hands with clean, running water (warm or cold), turn off the tap, and apply soap.
- Lather your hands by rubbing them together with the soap. Lather the backs of your hands, between your fingers, and under your nails.
- Scrub your hands for at least 20 seconds.
- Rinse your hands well under clean, running water.
- Dry your hands using a clean towel or air dry them.

```html
<!DOCTYPE html>
<html lang="en">
<head>
<meta charset="utf-8">
<title>How to Wash Your Hands</title>
<link href="https://fonts.googleapis.com/css2?family=Montserrat:ital,wght@0,500;0,700;0,800;1,800&display=swap" rel="stylesheet">
<style>
  :root {
    --navy: #2a3380;
    --ink: #12132f;
    --text: #1d1f3f;
    --badge: #c1473b;
    --white: #ffffff;
    --blush: #fbdedc;
    --hand-light: #b9bde3;
    --hand-mid: #7580bd;
    --water: #7fb0e0;
    --soap: #9a7bc0;
  }
  * { margin: 0; padding: 0; box-sizing: border-box; }
  html, body { width: 943px; height: 1200px; overflow: hidden; }
  body { font-family: 'Montserrat', sans-serif; background: var(--blush); color: var(--text); }
  .poster { position: relative; width: 943px; height: 1200px; }
  .icon-library { position: absolute; width: 0; height: 0; overflow: hidden; }

  .wash-section { position: absolute; left: 0; top: 0; width: 943px; height: 918px; background: var(--navy); }
  .wash-card { position: absolute; left: 39px; top: 43px; width: 865px; height: 849px; background: var(--white); border-radius: 18px; }
  .wash-title { position: absolute; left: 0; top: 74px; width: 943px; text-align: center; font-weight: 800; font-size: 50px; letter-spacing: 0.4px; color: var(--navy); line-height: 1; }

  .step-art, .sanitizer-art { position: absolute; width: 171px; height: 171px; border-radius: 50%; overflow: hidden;
    background: radial-gradient(circle at 50% 62%, #6a72b4 0%, #3a4080 30%, #1d2050 52%, var(--ink) 72%); }
  .sanitizer-art { width: 172px; height: 172px; }
  .step-art svg, .sanitizer-art svg { width: 100%; height: 100%; display: block; color: var(--white); }

  .badge { position: absolute; width: 28px; height: 28px; border-radius: 50%; background: var(--badge);
    color: var(--white); font-weight: 700; font-size: 17px; line-height: 28px; text-align: center; font-style: normal; }
  .step-label { position: absolute; width: 190px; text-align: center; font-weight: 500; font-size: 13px; line-height: 14.2px; text-transform: uppercase; }

  .timing-note { position: absolute; left: 143px; top: 837px; height: 46px; display: flex; align-items: center; gap: 10px;
    font-weight: 800; font-style: italic; font-size: 15.5px; color: var(--ink); }
  .timing-note .badge { position: static; }
  .timer-icon { width: 46px; height: 46px; font-style: normal; }

  .sanitizer-title { position: absolute; left: 0; top: 937px; width: 943px; text-align: center; font-weight: 800; font-size: 32px; color: var(--navy); line-height: 1; }
  .sanitizer-label { position: absolute; font-weight: 500; font-size: 13px; line-height: 14.4px; text-transform: uppercase; }
</style>
</head>
<body>
<svg class="icon-library" aria-hidden="true">
  <defs>
    <symbol id="icon-drop" viewBox="0 0 40 40">
      <path d="M20 3C20 3 8 18 8 26a12 12 0 0 0 24 0C32 18 20 3 20 3Z" fill="currentColor"/>
    </symbol>
    <symbol id="icon-rotate" viewBox="0 0 40 40">
      <path d="M20 8A12 12 0 1 0 32 20" fill="none" stroke="currentColor" stroke-width="3" stroke-linecap="round"/>
      <path d="M14 3L20 8L15 13" fill="none" stroke="currentColor" stroke-width="3" stroke-linecap="round" stroke-linejoin="round"/>
    </symbol>
    <symbol id="icon-updown" viewBox="0 0 40 40">
      <path d="M15 6V34M10 29L15 34L20 29" fill="none" stroke="currentColor" stroke-width="3" stroke-linecap="round" stroke-linejoin="round"/>
      <path d="M25 34V6M20 11L25 6L30 11" fill="none" stroke="currentColor" stroke-width="3" stroke-linecap="round" stroke-linejoin="round"/>
    </symbol>
    <symbol id="icon-cross" viewBox="0 0 40 40">
      <path d="M8 32L32 8M24 8H32V16" fill="none" stroke="currentColor" stroke-width="3" stroke-linecap="round" stroke-linejoin="round"/>
      <path d="M32 32L8 8M8 16V8H16" fill="none" stroke="currentColor" stroke-width="3" stroke-linecap="round" stroke-linejoin="round"/>
    </symbol>
    <symbol id="icon-plus" viewBox="0 0 10 10">
      <path d="M5 0V10M0 5H10" stroke="currentColor" stroke-width="1.6"/>
    </symbol>
    <symbol id="icon-tick" viewBox="0 0 40 40">
      <path d="M8 21L17 30L33 11" fill="none" stroke="currentColor" stroke-width="4" stroke-linecap="round" stroke-linejoin="round"/>
    </symbol>
  </defs>
</svg>

<div class="poster">
  <section class="wash-section">
    <div class="wash-card"></div>
    <h1 class="wash-title">HOW TO WASH YOUR HANDS</h1>

    <!-- Row 1 -->
    <div class="step-art" style="left:77px;top:144px" role="img" aria-label="Hands wetted under a running tap">
      <svg viewBox="0 0 171 171"><use href="#icon-drop" x="52" y="55" width="28" height="28" style="color:var(--water)"/><use href="#icon-drop" x="86" y="78" width="34" height="34" style="color:var(--water)"/><use href="#icon-drop" x="64" y="100" width="24" height="24" style="color:var(--water)"/></svg>
    </div>
    <div class="badge" style="left:73px;top:142px">1</div>
    <p class="step-label" style="left:67px;top:321px">Wet hands with<br>clean, running<br>water</p>

    <div class="step-art" style="left:285px;top:144px" role="img" aria-label="Soap dispensed onto a palm">
      <svg viewBox="0 0 171 171"><use href="#icon-drop" x="60" y="55" width="52" height="52" style="color:var(--soap)"/><use href="#icon-plus" x="79" y="83" width="14" height="14"/></svg>
    </div>
    <div class="badge" style="left:282px;top:142px">2</div>
    <p class="step-label" style="left:275px;top:321px">Turn off the tap,<br>and apply soap</p>

    <div class="step-art" style="left:492px;top:144px" role="img" aria-label="Hands rubbing palm to palm">
      <svg viewBox="0 0 171 171"><use href="#icon-rotate" x="58" y="58" width="56" height="56"/></svg>
    </div>
    <div class="badge" style="left:488px;top:142px">3</div>
    <p class="step-label" style="left:482px;top:320px">Rub hands<br>palm to palm</p>

    <div class="step-art" style="left:700px;top:144px" role="img" aria-label="Lathering the back of the hands">
      <svg viewBox="0 0 171 171"><use href="#icon-updown" x="58" y="58" width="56" height="56"/></svg>
    </div>
    <div class="badge" style="left:696px;top:142px">4</div>
    <p class="step-label" style="left:690px;top:320px">Lather the back<br>of both hands</p>

    <!-- Row 2 -->
    <div class="step-art" style="left:77px;top:373px" role="img" aria-label="Scrubbing between interlaced fingers">
      <svg viewBox="0 0 171 171"><use href="#icon-cross" x="60" y="60" width="52" height="52"/></svg>
    </div>
    <div class="badge" style="left:73px;top:373px">5</div>
    <p class="step-label" style="left:67px;top:548px">Scrub between<br>your fingers</p>

    <div class="step-art" style="left:285px;top:373px" role="img" aria-label="Rubbing the back of fingers on the opposing palm">
      <svg viewBox="0 0 171 171"><use href="#icon-updown" x="58" y="58" width="56" height="56" transform="rotate(30 86 86)"/></svg>
    </div>
    <div class="badge" style="left:282px;top:373px">6</div>
    <p class="step-label" style="left:275px;top:550px;font-size:11.4px;line-height:14px">Rub the back of<br>fingers on the<br>opposing palm</p>

    <div class="step-art" style="left:492px;top:373px" role="img" aria-label="Rotating a thumb inside the other hand">
      <svg viewBox="0 0 171 171"><use href="#icon-rotate" x="58" y="58" width="56" height="56" transform="scale(-1 1) translate(-171 0)"/></svg>
    </div>
    <div class="badge" style="left:488px;top:373px">7</div>
    <p class="step-label" style="left:482px;top:553px">Clean thumbs</p>

    <div class="step-art" style="left:700px;top:373px" role="img" aria-label="Fingertips rubbed against the palm">
      <svg viewBox="0 0 171 171"><use href="#icon-rotate" x="58" y="58" width="56" height="56"/></svg>
    </div>
    <div class="badge" style="left:696px;top:373px">8</div>
    <p class="step-label" style="left:690px;top:550px">Wash fingernails<br>and fingertips</p>

    <!-- Row 3 -->
    <div class="step-art" style="left:77px;top:602px" role="img" aria-label="Hands rinsed under a running tap">
      <svg viewBox="0 0 171 171"><use href="#icon-drop" x="56" y="50" width="30" height="30" style="color:var(--water)"/><use href="#icon-drop" x="82" y="72" width="36" height="36" style="color:var(--water)"/><use href="#icon-drop" x="58" y="96" width="26" height="26" style="color:var(--water)"/></svg>
    </div>
    <div class="badge" style="left:73px;top:596px">9</div>
    <p class="step-label" style="left:67px;top:782px">Rinse hands well<br>under clean,<br>running water</p>

    <div class="step-art" style="left:285px;top:602px" role="img" aria-label="Hands dried with a single use towel">
      <svg viewBox="0 0 171 171"><rect x="56" y="56" width="60" height="60" rx="6" fill="var(--white)"/><path d="M66 74H106M66 86H106M66 98H96" stroke="var(--hand-light)" stroke-width="3" stroke-linecap="round"/></svg>
    </div>
    <div class="badge" style="left:282px;top:596px">10</div>
    <p class="step-label" style="left:275px;top:781px">Dry with a<br>single use towel</p>

    <div class="step-art" style="left:492px;top:602px" role="img" aria-label="Towel used to turn off the faucet">
      <svg viewBox="0 0 171 171"><rect x="50" y="62" width="70" height="8" rx="4" fill="var(--white)"/><rect x="80" y="70" width="12" height="22" fill="var(--white)"/><use href="#icon-drop" x="76" y="100" width="20" height="20" style="color:var(--water)"/></svg>
    </div>
    <div class="badge" style="left:488px;top:596px">11</div>
    <p class="step-label" style="left:482px;top:782px">Use the towel<br>to turn off the<br>faucet</p>

    <div class="step-art" style="left:700px;top:602px" role="img" aria-label="Two clean hands with sparkles">
      <svg viewBox="0 0 171 171"><use href="#icon-plus" x="72" y="24" width="10" height="10"/><use href="#icon-plus" x="50" y="42" width="9" height="9"/><use href="#icon-plus" x="92" y="40" width="9" height="9"/><use href="#icon-plus" x="118" y="48" width="9" height="9"/><use href="#icon-plus" x="30" y="70" width="8" height="8"/><use href="#icon-plus" x="138" y="78" width="8" height="8"/><use href="#icon-tick" x="60" y="70" width="52" height="52"/></svg>
    </div>
    <div class="badge" style="left:696px;top:596px">12</div>
    <p class="step-label" style="left:690px;top:783px">Your hands are<br>clean</p>

    <div class="timing-note">
      <svg class="timer-icon" viewBox="0 0 46 46" aria-hidden="true">
        <rect x="19" y="1" width="8" height="4" rx="1" fill="var(--ink)"/>
        <rect x="5" y="7" width="6" height="3" rx="1" transform="rotate(-40 8 8)" fill="var(--ink)"/>
        <rect x="35" y="7" width="6" height="3" rx="1" transform="rotate(40 38 8)" fill="var(--ink)"/>
        <circle cx="23" cy="25" r="20" fill="var(--ink)"/>
        <text x="23" y="30" text-anchor="middle" font-family="Montserrat, sans-serif" font-style="normal" font-weight="700" font-size="18" fill="#fff">20</text>
        <text x="23" y="38" text-anchor="middle" font-family="Montserrat, sans-serif" font-style="normal" font-weight="500" font-size="4.6" fill="#fff">SECONDS</text>
      </svg>
      <span>FROM</span>
      <span class="badge">3</span>
      <span>TO</span>
      <span class="badge">8</span>
      <span>:&nbsp;&nbsp;SCRUB YOUR HANDS FOR AT LEAST 20 SECONDS.</span>
    </div>
  </section>

  <section class="sanitizer-section">
    <h2 class="sanitizer-title">APPLICATION OF HAND SANITIZER</h2>

    <div class="sanitizer-art" style="left:37px;top:989px" role="img" aria-label="Sanitizer dispensed onto the palm of one hand">
      <svg viewBox="0 0 172 172"><rect x="68" y="14" width="36" height="40" rx="5" fill="var(--white)"/><use href="#icon-plus" x="80" y="27" width="12" height="12" style="color:var(--ink)"/><use href="#icon-drop" x="70" y="70" width="32" height="32" style="color:var(--soap)"/></svg>
    </div>
    <div class="badge" style="left:218px;top:998px">1</div>
    <p class="sanitizer-label" style="left:218px;top:1035px">Apply the<br>product on<br>the palm of<br>one hand</p>

    <div class="sanitizer-art" style="left:334px;top:989px" role="img" aria-label="Hands rubbing sanitizer together">
      <svg viewBox="0 0 172 172"><use href="#icon-rotate" x="58" y="58" width="56" height="56"/></svg>
    </div>
    <div class="badge" style="left:511px;top:998px">2</div>
    <p class="sanitizer-label" style="left:511px;top:1035px">Rub hands<br>together</p>

    <div class="sanitizer-art" style="left:621px;top:989px" role="img" aria-label="Hands drying with a twenty second timer">
      <svg viewBox="0 0 172 172">
        <path d="M58 24c-6 8 6 14 0 22s6 14 0 22M74 24c-6 8 6 14 0 22s6 14 0 22M90 24c-6 8 6 14 0 22s6 14 0 22" fill="none" stroke="var(--white)" stroke-width="3" stroke-linecap="round"/>
        <rect x="128" y="52" width="10" height="4" rx="1" fill="var(--white)"/>
        <circle cx="133" cy="80" r="22" fill="var(--white)"/>
        <text x="133" y="86" text-anchor="middle" font-family="Montserrat, sans-serif" font-weight="700" font-size="19" fill="var(--ink)">20</text>
        <text x="133" y="94" text-anchor="middle" font-family="Montserrat, sans-serif" font-weight="500" font-size="4.8" fill="var(--ink)">SECONDS</text>
      </svg>
    </div>
    <div class="badge" style="left:800px;top:998px">3</div>
    <p class="sanitizer-label" style="left:802px;top:1035px">Cover all<br>surfaces<br>until hands<br>feel dry<br>(20 sec)</p>
  </section>
</div>
</body>
</html>
```